Fitness company needs new web design

We are looking to get our current site design improved to a newer design to better match our logo and features.

Current Site:
brivanfitco.com

* We would like the site to be modern/simple.
* The site will need to have the ability to take payments via paylune.
* We would like a "shop" page, as we will be selling supplements. Possible linkup with Cartwell.
* The main landing page should flow in a way to sell our personal training & diet services. We would like the user to have to input their info (like we currently have) before placing an order.

We like how this site is put together: lumaxrt.com

We use this service for our mobile app that our clients get to use when they signup: coachvelo.net

If you have any questions please message use before starting your design.

Target Market(s)

Weight Loss, Fitness, Sports Athletes

Industry/Entity Type

Fitness

Coding

Coded - Design and coding required

Number of Pages Required

5+ page

Colors

Designer to choose colors to be used in the design.

Requirements
Must have
• Menu Tabs:
• - Programs
• - We offer 3 programs (see below for complete details)
• * Basic
• * Premium
• * Elite
• - Supplements
• - We currently have 2 supplements (see attached labels)
• * Nova Lift
• * Nova Flare
• - About
• - FAQ
• - Contact
• - Book Appointment (bookwisp.com)
• Program Breakdown:
• Basic: Price $99/month
• - One 30 Minute In-Person or Phone Consultation
• - Unlimited in-app text support
• - Basic Nutrition Education
• - 30 Day Meal Plan
• Premium: Price $149/month
• - Two 30 Minute In-Person or Phone Consultations
• - Unlimited In-App Messaging Support
• - Customized Strength Training Program
• - Each Exercise Demonstrated in HD Videos
• - Personalized Cardio Program
• - Personalized Nutrition Coaching & Meal Plans
• Elite: Price $249/month
• - Weekly 30 Minute In-Person or Phone Consultation
• - Weekly Customized Strength Training Program
• - Weekly Customized Cardio Training Program
• - Bi-Weekly Nutrition Coaching & Meal Plans
Nice to have
• Click through form that collects clients information (like we have on our current site brivanfitco.com

```html
<!DOCTYPE html>
<html lang="en">
<head>
<meta charset="utf-8">
<title>Brivan Fitco — Online Personal Coaching</title>
<link rel="stylesheet" href="https://fonts.googleapis.com/css2?family=Open+Sans:wdth,wght@75..100,400..800&family=Arimo:wght@400;700&display=swap">
<style>
:root{
  --yellow:#f5ee1b;
  --black:#111111;
  --ink:#222222;
  --grey:#6b6b6b;
  --panel:#666666;
  --charcoal:#2b2b2b;
  --footer:#2a2a2a;
  --muted:#555555;
  --white:#ffffff;
}
*{box-sizing:border-box;margin:0;padding:0}
html,body{width:1200px;height:4286px;overflow:hidden}
body{font-family:"Open Sans",sans-serif;color:var(--ink);background:var(--white);position:relative}
section,header,footer{position:absolute;left:0;width:1200px}

/* Header */
.site-header{top:0;height:143px;background:var(--white)}
.brand-block{position:absolute;left:0;top:0;width:390px;height:143px;background:var(--black);clip-path:polygon(0 0,100% 0,78% 100%,0 100%);display:flex;align-items:center;padding-left:96px;gap:14px}
.brand-dot{width:22px;height:22px;border-radius:50%;background:var(--yellow)}
.brand-name{font-weight:700;font-size:22px;color:var(--yellow);letter-spacing:1px;text-transform:uppercase}
.cart{position:absolute;left:733px;top:28px;display:flex;align-items:center;gap:10px;font-size:16px;color:var(--grey)}
.cart-icon{width:34px;height:34px;border-radius:50%;background:#777;display:flex;align-items:center;justify-content:center}
.book-btn{position:absolute;left:914px;top:18px;height:50px;display:flex;font-weight:700;font-size:16px;text-transform:uppercase}
.book-btn .b1{background:var(--yellow);color:var(--black);padding:0 8px 0 12px;display:flex;align-items:center}
.book-btn .b2{background:#7a7a7a;color:var(--white);padding:0 12px 0 20px;display:flex;align-items:center;clip-path:polygon(14px 0,100% 0,100% 100%,0 100%);margin-left:-10px}
.main-nav{position:absolute;right:40px;top:92px;display:flex;gap:34px;font-weight:600;font-size:16px;text-transform:uppercase;font-stretch:80%}
.main-nav a{color:var(--black);text-decoration:none}

/* Hero */
.hero{top:143px;height:514px;background:linear-gradient(90deg,#2a2d31 0%,#4a4d52 45%,#3a3c40 75%,#24262a 100%)}
.hero-photo{position:absolute;inset:0}
.hero-copy{position:absolute;left:97px;top:60px;width:620px;color:var(--white)}
.hero-copy h1{font-size:46px;font-weight:700;line-height:1.25;font-stretch:80%}
.hero-copy p{font-size:15px;line-height:1.6;margin-top:22px;width:540px}
.btn-outline{display:inline-block;margin-top:24px;border:2px solid var(--white);color:var(--white);font-weight:700;font-size:14px;padding:14px 22px;text-transform:uppercase;text-decoration:none;font-stretch:80%}
.hero-dots{position:absolute;left:97px;top:398px;display:flex;gap:6px}
.hero-dots span{width:20px;height:20px;border-radius:50%;background:#aaa}
.hero-dots span.on{background:var(--yellow)}

/* Welcome */
.welcome{top:657px;height:453px;text-align:center}
.section-title{font-size:40px;font-weight:700;font-stretch:80%;color:var(--ink)}
.welcome .section-title{margin-top:68px}
.divider{position:absolute;left:97px;right:97px;top:190px;height:2px;background:#999}
.divider-mark{position:absolute;left:50%;top:-36px;width:72px;height:72px;margin-left:-36px;border-radius:50%;background:var(--white);border:6px solid var(--yellow)}
.welcome p{position:absolute;left:195px;width:810px;top:262px;font-size:15px;line-height:1.75;color:var(--muted)}

/* Features */
.features{top:1110px;height:770px}
.feature{position:absolute;width:600px;height:385px}
.panel{background:var(--panel);display:flex;flex-direction:column;align-items:center;justify-content:center;text-align:center;color:var(--white)}
.panel h2{color:var(--yellow);font-size:34px;font-weight:700;line-height:1.3;font-stretch:80%;text-transform:uppercase}
.panel p{font-size:19px;line-height:2.2;margin-top:14px}
.panel-left::before{content:"";position:absolute;left:0;top:0;width:80px;height:100%;background:var(--yellow);clip-path:polygon(0 0,100% 0,20% 100%,0 100%)}
.panel-right::after{content:"";position:absolute;right:0;top:0;width:70px;height:100%;background:var(--yellow);clip-path:polygon(100% 0,100% 100%,0 100%,60% 0)}
.photo{display:flex;align-items:center;justify-content:center}
.photo-a{background:linear-gradient(135deg,#6c6560 0%,#3a3634 60%,#2c2a28 100%)}
.photo-b{background:linear-gradient(135deg,#d9dce0 0%,#a9aeb4 55%,#5a6f8a 100%)}
.play{width:70px;height:70px}

/* Success */
.success{top:1880px;height:690px;text-align:center}
.success .section-title{margin-top:76px}
.success .lead{font-size:16px;color:var(--muted);margin-top:16px}
.perks{position:absolute;left:97px;top:230px;width:1006px;display:flex;justify-content:space-between}
.perk{width:240px;display:flex;flex-direction:column;align-items:center}
.perk-icon{width:164px;height:164px;border-radius:50%;display:flex;align-items:center;justify-content:center}
.perk-icon.dark{background:#666;border:5px solid #444}
.perk-icon.light{background:#666;border:7px solid var(--yellow)}
.perk h3{font-size:19px;font-weight:700;margin-top:22px;line-height:1.4;min-height:54px;color:#333;font-stretch:85%}
.perk p{font-size:13px;line-height:1.6;color:var(--muted);margin-top:14px}

/* Guarantee */
.guarantee{top:2571px;height:449px;background:linear-gradient(90deg,#151515 0%,#262626 70%,#1a1a1a 100%)}
.guarantee-photo{position:absolute;right:0;top:0;width:420px;height:449px;background:linear-gradient(135deg,#f5ee1b 0%,#e6d84a 45%,#5a5040 46%,#2a2520 100%)}
.guarantee-copy{position:absolute;left:97px;top:165px;width:720px;color:var(--white)}
.guarantee-copy h2{color:var(--yellow);font-size:38px;font-weight:700;font-stretch:80%}
.guarantee-copy p{font-size:16px;line-height:1.75;margin-top:18px;text-transform:uppercase}
.plan-btn{display:inline-flex;margin-top:20px;font-weight:700;font-size:14px;text-transform:uppercase;height:48px;font-stretch:85%}
.plan-btn .p1{background:var(--yellow);color:var(--black);display:flex;align-items:center;padding:0 8px}
.plan-btn .p2{background:#7a7a7a;color:var(--yellow);display:flex;align-items:center;padding:0 14px}

/* Testimonials */
.testimonials{top:3020px;height:720px;text-align:center}
.testimonials .section-title{margin-top:70px}
.title-rule{width:105px;height:2px;background:#333;margin:20px auto 0}
.quotes{position:absolute;left:97px;top:215px;width:1030px;display:flex;justify-content:space-between;text-align:left}
.quote{width:320px}
.quote-mark{font-family:Arimo,sans-serif;font-size:100px;font-weight:700;line-height:0.7;height:40px;color:var(--black);font-style:italic}
.quote h3{font-family:Arimo,sans-serif;font-size:31px;font-weight:700;line-height:1.25;margin-top:10px;color:var(--black)}
.quote p{font-family:Arimo,sans-serif;font-size:12.5px;line-height:1.6;color:var(--muted);margin-top:14px}
.read-more{display:block;font-family:Arimo,sans-serif;font-size:14px;font-weight:700;margin-top:18px;color:var(--black);text-decoration:none}
.slider-bars{position:absolute;left:500px;top:620px;display:flex;gap:6px}
.slider-bars span{width:60px;height:3px;background:#777}
.slider-bars span.on{background:var(--yellow)}

/* Newsletter */
.newsletter{top:3740px;height:80px;background:var(--yellow);display:flex;align-items:center;padding-left:97px}
.newsletter label{font-size:26px;font-weight:700;color:var(--black);font-stretch:80%}
.newsletter .field{width:610px;height:46px;border:2px solid var(--black);background:var(--yellow);margin-left:18px}
.newsletter .submit{margin-left:14px;background:var(--black);color:var(--white);font-weight:700;font-size:15px;height:46px;padding:0 16px;display:flex;align-items:center;text-transform:uppercase;font-stretch:85%}

/* Footer */
.site-footer{top:3820px;height:466px;background:var(--footer);text-align:center;color:var(--white)}
.footer-brand{margin-top:86px;display:flex;align-items:center;justify-content:center;gap:14px}
.footer-brand .brand-dot{width:26px;height:26px}
.footer-brand .brand-name{font-size:24px}
.socials{margin-top:66px;display:flex;justify-content:center;gap:12px}
.socials span{width:46px;height:46px;border-radius:50%;border:3px solid var(--white)}
.footer-nav{margin-top:34px;font-size:15px;font-weight:600;text-transform:uppercase;word-spacing:2px}
.footer-nav span{margin:0 12px;color:var(--white)}
.footer-rule{position:absolute;left:97px;right:97px;top:370px;height:1px;background:#777}
.copyright{position:absolute;left:0;right:0;top:405px;font-size:13px;font-weight:700}
</style>
</head>
<body>

<header class="site-header">
  <div class="brand-block"><span class="brand-dot"></span><span class="brand-name">Brivan Fitco</span></div>
  <div class="cart">
    <span class="cart-icon">
      <svg width="18" height="18" viewBox="0 0 18 18"><path d="M3 6h12l-1.5 9h-9z" fill="#fff"/><path d="M6 6V4a3 3 0 0 1 6 0v2" stroke="#fff" stroke-width="1.6" fill="none"/></svg>
    </span>
    <span>Cart: 0 Items</span>
  </div>
  <div class="book-btn"><span class="b1">Book</span><span class="b2">Appointment</span></div>
  <nav class="main-nav">
    <a href="#">Home</a><a href="#">Programs</a><a href="#">Supplements</a><a href="#">About</a><a href="#">FAQ</a><a href="#">Contact</a>
  </nav>
</header>

<section class="hero">
  <div class="hero-photo" role="img" aria-label="Coach and client reviewing a tablet together in a gym"></div>
  <div class="hero-copy">
    <h1>Stop Dieting and Start Losing<br>more Weight Faster!</h1>
    <p>Brivan Fitco is a 100% custom online personal coaching program for those looking to burn fat while building a lean athletic body.</p>
    <a class="btn-outline" href="#">Read More</a>
  </div>
  <div class="hero-dots"><span class="on"></span><span></span><span></span><span></span><span></span></div>
</section>

<section class="welcome">
  <h2 class="section-title">Welcome To Brivan Fitco</h2>
  <div class="divider"><span class="divider-mark"></span></div>
  <p>Unlike the average carb fueled diets that eat into your muscles energy stores, ketosis preserves your body's ability to retain glycogen during physical activities while increasing fat oxidation. Since your body is using it's nearly unlimited fat stores for fuel, it mobilizes the fat for fuel and preserves precious muscle mass.</p>
</section>

<section class="features">
  <div class="feature panel panel-left" style="left:0;top:0">
    <h2>Discover How You Can<br>Burn Fat</h2>
    <p>and build a lean body at the same time!</p>
  </div>
  <div class="feature photo photo-a" style="left:600px;top:0" role="img" aria-label="Man with headphones checking his phone beside kettlebells">
    <svg class="play" viewBox="0 0 70 70"><circle cx="35" cy="35" r="32" fill="none" stroke="#fff" stroke-width="4"/><path d="M28 22l20 13-20 13z" fill="#fff"/></svg>
  </div>
  <div class="feature photo photo-b" style="left:0;top:385px" role="img" aria-label="Man doing push-ups on a mat in front of a laptop">
    <svg class="play" viewBox="0 0 70 70"><circle cx="35" cy="35" r="32" fill="none" stroke="#fff" stroke-width="4"/><path d="M28 22l20 13-20 13z" fill="#fff"/></svg>
  </div>
  <div class="feature panel panel-right" style="left:600px;top:385px">
    <h2>Increase Your Mental Sharpness<br>and Clarity</h2>
    <p>Reduce "brain fog" and feel more alert<br>throughout your day</p>
  </div>
</section>

<section class="success">
  <h2 class="section-title">Your Success Is Our Success</h2>
  <p class="lead">Don't be just another sale, join a community of like-minded people that want to see you succeed!</p>
  <div class="perks">
    <div class="perk">
      <div class="perk-icon dark">
        <svg width="80" height="80" viewBox="0 0 80 80" fill="none" stroke="#f5ee1b" stroke-width="3"><path d="M40 8l18 7v14c0 10-8 16-18 20-10-4-18-10-18-20V15z"/><path d="M32 28l6 6 10-12"/><circle cx="24" cy="54" r="6"/><circle cx="40" cy="52" r="7"/><circle cx="56" cy="54" r="6"/><path d="M12 74c0-8 6-12 12-12s12 4 12 12M28 74c0-9 5-14 12-14s12 5 12 14M44 74c0-8 6-12 12-12s12 4 12 12"/></svg>
      </div>
      <h3>Private Online<br>Community</h3>
      <p>Join our team and others like you in our private Chatterly group. Share receipts, goals, training techniques, and results. The Brivan Fitco community is there to support you 24 hours a day, 7 days a week!</p>
    </div>
    <div class="perk">
      <div class="perk-icon light">
        <svg width="80" height="80" viewBox="0 0 80 80" fill="none" stroke="#fff" stroke-width="3"><path d="M40 46V26M40 30c-4-10-14-10-18-6 6 6 12 8 18 6zM40 30c4-10 14-10 18-6-6 6-12 8-18 6z"/><path d="M8 58h12l10 4h16a4 4 0 0 1 0 8H30M46 66l16-8a4 4 0 0 1 6 5L48 74H20"/></svg>
      </div>
      <h3>Weekly Accountability<br>Calls</h3>
      <p>Each week the Brivan Fitco team will hold a weekly accountability call to answer any questions, as well as, get an update on everyone's results. This is a great way to stay on track.</p>
    </div>
    <div class="perk">
      <div class="perk-icon dark">
        <svg width="80" height="80" viewBox="0 0 80 80" fill="none" stroke="#f5ee1b" stroke-width="3"><rect x="10" y="10" width="28" height="20" rx="3"/><rect x="42" y="16" width="28" height="20" rx="3"/><circle cx="26" cy="48" r="7"/><circle cx="54" cy="48" r="7"/><path d="M12 72c0-8 6-12 14-12s14 4 14 12M40 72c0-8 6-12 14-12s14 4 14 12"/></svg>
      </div>
      <h3>Unlimited Text &amp; Email<br>Support</h3>
      <p>99% of online personal training sites only allow for one email per week and most programs do not offer any type of text support. The Brivan Fitco team thinks different - your success is our success.</p>
    </div>
    <div class="perk">
      <div class="perk-icon light">
        <svg width="80" height="80" viewBox="0 0 80 80" fill="none" stroke="#fff" stroke-width="3"><rect x="10" y="14" width="60" height="40" rx="3"/><path d="M30 64h20M40 54v10M16 36h12l4-10 6 18 5-12 4 4h17"/></svg>
      </div>
      <h3>Member<br>Portal Access</h3>
      <p>From food lists to workout videos. You will have access to your very own member portal where you can log your goals, update your results, and get your questions answered fast!</p>
    </div>
  </div>
</section>

<section class="guarantee">
  <div class="guarantee-photo" role="img" aria-label="Athletic woman in sports wear with boxing wraps against a yellow backdrop"></div>
  <div class="guarantee-copy">
    <h2>30 Day Money Back Guarantee!</h2>
    <p>If you do not experience the results you should by the efforts you put in, we will refund 100% of the cost of the program. So what do you have to lose... besides fat!?</p>
    <span class="plan-btn"><span class="p1">Get My</span><span class="p2">Customized Plan</span></span>
  </div>
</section>

<section class="testimonials">
  <h2 class="section-title">Our Testimonials</h2>
  <div class="title-rule"></div>
  <div class="quotes">
    <article class="quote">
      <div class="quote-mark">"</div>
      <h3>Nemo enim ipsam voluptatem quia</h3>
      <p>Sed ut perspiciatis unde omnis iste natus error sit vo luptatem accusantium doloremque laudan tium, totam rem aperiam, eaque ipsa quae ab illo inventore veritatis et quasi architecto beatae vitae dicta sunt explicabo.</p>
      <a class="read-more" href="#">Read More &gt;&gt;</a>
    </article>
    <article class="quote">
      <div class="quote-mark">"</div>
      <h3>Nemo enim ipsam voluptatem quia</h3>
      <p>Sed ut perspiciatis unde omnis iste natus error sit vo luptatem accusantium doloremque laudan tium, totam rem aperiam, eaque ipsa quae ab illo inventore veritatis et quasi architecto beatae vitae dicta sunt explicabo.</p>
      <a class="read-more" href="#">Read More &gt;&gt;</a>
    </article>
    <article class="quote">
      <div class="quote-mark">"</div>
      <h3>Nemo enim ipsam voluptatem quia</h3>
      <p>Sed ut perspiciatis unde omnis iste natus error sit vo luptatem accusantium doloremque laudan tium, totam rem aperiam, eaque ipsa quae ab illo inventore veritatis et quasi architecto beatae vitae dicta sunt explicabo.</p>
      <a class="read-more" href="#">Read More &gt;&gt;</a>
    </article>
  </div>
  <div class="slider-bars"><span class="on"></span><span></span><span></span></div>
</section>

<section class="newsletter">
  <label>Newsletter Signup:</label>
  <span class="field"></span>
  <span class="submit">Signup Now</span>
</section>

<footer class="site-footer">
  <div class="footer-brand"><span class="brand-dot"></span><span class="brand-name">Brivan Fitco</span></div>
  <div class="socials"><span></span><span></span><span></span><span></span><span></span></div>
  <nav class="footer-nav">Home<span>|</span>Programs<span>|</span>Supplements<span>|</span>About<span>|</span>FAQ<span>|</span>Contact Us</nav>
  <div class="footer-rule"></div>
  <p class="copyright">Copyrights @ 2018 Brivan Fitco. All Rights Reserved.</p>
</footer>

</body>
</html>
```